Gluten Cove - cover photos - facebooks groups

I have a logo - gluten cove. I have 2 groups that I need cover photos for with the new brand.

Gluten Cove - All Inclusive Reviews

Gluten Cove - Travel Deals

Two separate groups *powered by Journey Crest* at the bottom of the travel deals in fine print. Not the all inclusive group - that’s powered by 2 agencies - at the bottom powered by 2 celiac travel agents.

I want to keep with the current theme. Maybe the logo, and colour dark block on the left (or whatever standard format to make more going forward) then the versions: deals and all inclusive reviews to the right. Happy, simple, clean. Not cheesy. Match the brand and logo to the group.

Attached are the two current cover photos. (To peach!!) I want the pictures and brand to align with the logo. Happy beach - all inclusive. And international travel and fancy cruise for the travel deals.

I’d like a corporate look that we can scale with any new launch.

Thanks!

```html
<!DOCTYPE html>
<html lang="en">
<head>
<meta charset="utf-8">
<title>Gluten Cove – Group Cover Banners</title>
<link href="https://fonts.googleapis.com/css2?family=Sacramento&family=Courier+Prime:wght@700&family=Open+Sans:wght@600&display=swap" rel="stylesheet">
<style>
  :root {
    --page-bg: #a7a8ac;
    --navy: #14283f;
    --white: #ffffff;
    --sky: #8d8a86;
    --sea: #2f8a8c;
    --sea-deep: #1f6f75;
    --sand: #b69a86;
    --sand-light: #cdb3a0;
  }
  * { margin: 0; padding: 0; box-sizing: border-box; }
  html, body {
    width: 1200px; height: 1200px; overflow: hidden;
    background: var(--page-bg);
  }
  .banner-stack {
    position: absolute; left: 50px; top: 160px;
    display: flex; flex-direction: column; gap: 64px;
  }
  .cover {
    position: relative; width: 1100px; height: 408px; overflow: hidden;
  }
  .cover-photo {
    position: absolute; inset: 0;
    background:
      radial-gradient(ellipse 260px 90px at 300px 70px, rgba(240,190,140,.85), rgba(240,190,140,0) 70%),
      linear-gradient(160deg, var(--sky) 0%, #9b8e86 14%, var(--sea-deep) 22%, var(--sea) 38%, #6f9a98 52%, var(--sand-light) 62%, var(--sand) 100%);
  }
  .cover-photo::after {
    content: ""; position: absolute; inset: 0;
    background: linear-gradient(100deg, rgba(190,160,140,.55) 0%, rgba(190,160,140,.25) 45%, rgba(0,0,0,0) 70%);
  }
  .inner-frame {
    position: absolute; left: 44px; top: 24px; right: 41px; bottom: 25px;
    border: 2px solid rgba(255,255,255,.9);
  }
  .corner-block {
    position: absolute; left: 0; top: 0; width: 150px; height: 212px;
  }
  .brand-name {
    position: absolute; left: 20px; top: 30px;
    font: 700 11px "Courier Prime", monospace;
    color: var(--white); letter-spacing: .5px; white-space: nowrap;
  }
  .cover-title {
    position: absolute; left: 0; right: 0; top: 80px; text-align: center;
    font: 400 150px/1 "Sacramento", cursive;
    color: var(--white);
    text-shadow: 3px 4px 6px rgba(0,0,0,.55);
    padding-left: 20px;
  }
  .cover-subtitle {
    position: absolute; left: 0; right: 0; top: 254px; text-align: center;
    font: 700 22px "Courier Prime", monospace;
    color: var(--white); letter-spacing: 5px;
    text-shadow: 1px 1px 3px rgba(0,0,0,.4);
    padding-left: 20px;
  }
  .powered-pill {
    position: absolute; left: 454px; top: 369px; width: 192px; height: 18px;
    border-radius: 5px; background: var(--navy);
    font: 600 10px/18px "Open Sans", sans-serif; letter-spacing: 1px;
    color: var(--white); text-align: center; white-space: nowrap;
  }
</style>
</head>
<body>
<main class="banner-stack">

  <section class="cover cover--reviews">
    <div class="cover-photo" role="img" aria-label="Sunset beach with turquoise waves washing onto the sand"></div>
    <div class="inner-frame"></div>
    <svg class="corner-block" viewBox="0 0 150 212" aria-hidden="true"><polygon points="0,0 150,0 0,212" fill="#14283f"/></svg>
    <div class="brand-name">Gluten Cove</div>
    <h1 class="cover-title">Gluten Cove</h1>
    <p class="cover-subtitle">All Inclusive Reviews</p>
    <div class="powered-pill">powered by 2 travel agents</div>
  </section>

  <section class="cover cover--deals">
    <div class="cover-photo" role="img" aria-label="Sunset beach with turquoise waves washing onto the sand"></div>
    <div class="inner-frame"></div>
    <svg class="corner-block" viewBox="0 0 150 212" aria-hidden="true"><polygon points="0,0 150,0 0,212" fill="#14283f"/></svg>
    <div class="brand-name">Gluten Cove</div>
    <h1 class="cover-title">Gluten Cove</h1>
    <p class="cover-subtitle">Travel Deals</p>
    <div class="powered-pill">powered by Journey Crest</div>
  </section>

</main>
</body>
</html>
```